Real Estate Card Design

I need a new business card! Below you will find my headshot, the company logo and a copy of my previous business card.

The card must contain the following information:

Dana Welloby
Sales Representative
HARBOURVIEW HOMES REALTY INC BROKERGE
204-517 Ashgrove Ave E, Oshawa ON L1H 4T6
Cell: 905-631-4872 Office:905-418-2096
www.danawelloby.example dana@homesbydana.example

I would like the card to portray security and class all the while being fresh and contemporary. I hold the key....

```html
<!DOCTYPE html>
<html lang="en">
<head>
<meta charset="utf-8">
<title>Dana Welloby – Business Card</title>
<link rel="stylesheet" href="https://fonts.googleapis.com/css2?family=Mulish:ital,wght@0,400;0,700;0,800;1,300;1,700&display=swap">
<style>
  :root {
    --backdrop: #7d7e83;
    --card-white: #ffffff;
    --brand-blue: #22a4de;
    --accent-navy: #263b49;
    --ink: #111111;
    --photo-dark: #1a1a1c;
    --photo-warm: #6b5a52;
  }
  html, body {
    margin: 0;
    padding: 0;
    width: 1200px;
    height: 913px;
    overflow: hidden;
    background: var(--backdrop);
  }
  .canvas {
    position: relative;
    width: 1200px;
    height: 913px;
  }
  .business-card {
    position: absolute;
    left: 75px;
    top: 156px;
    width: 1050px;
    height: 600px;
    box-shadow: 0 18px 40px rgba(0,0,0,0.35);
  }
  .business-card svg { display: block; }
  .card-text { font-family: 'Mulish', sans-serif; }
  .agent-name { font-weight: 800; font-size: 58px; fill: var(--card-white); }
  .agent-title { font-weight: 300; font-style: italic; font-size: 28px; fill: var(--card-white); }
  .brokerage-name { font-weight: 700; font-size: 27px; fill: var(--ink); letter-spacing: 1px; }
  .contact-line { font-weight: 700; font-style: italic; font-size: 31px; fill: var(--ink); }
  .contact-icon { fill: var(--ink); }
</style>
</head>
<body>
<div class="canvas">
  <div class="business-card">
    <svg width="1050" height="600" viewBox="0 0 1050 600" xmlns="http://www.w3.org/2000/svg">
      <defs>
        <radialGradient id="headshotTone" cx="45%" cy="45%" r="60%">
          <stop offset="0%" stop-color="var(--photo-warm)"/>
          <stop offset="100%" stop-color="var(--photo-dark)"/>
        </radialGradient>
      </defs>

      <!-- card base -->
      <rect class="card-base" width="1050" height="600" fill="var(--card-white)"/>

      <!-- blue header band -->
      <polygon class="brand-band" points="470,0 1050,0 1050,600 650,600" fill="var(--brand-blue)"/>
      <!-- navy accent -->
      <polygon class="accent-wedge" points="560,430 650,600 560,600" fill="var(--accent-navy)"/>
      <polygon class="accent-wedge" points="540,400 640,600 600,600" fill="var(--accent-navy)" opacity="0"/>

      <!-- headshot -->
      <circle cx="790" cy="190" r="142" fill="var(--card-white)"/>
      <circle cx="790" cy="190" r="132" fill="url(#headshotTone)" role="img" aria-label="Headshot of Dana Welloby"/>

      <!-- agent identity -->
      <text class="card-text agent-name" x="800" y="412" text-anchor="middle">Dana Welloby</text>
      <text class="card-text agent-title" x="800" y="458" text-anchor="middle">Sales Representative</text>

      <!-- brokerage name -->
      <rect class="brokerage-square" x="40" y="60" width="120" height="120" fill="var(--brand-blue)"/>
      <text class="card-text brokerage-name" x="180" y="98">HARBOURVIEW HOMES</text>
      <text class="card-text brokerage-name" x="180" y="134">REALTY INC</text>
      <text class="card-text brokerage-name" x="180" y="170">BROKERGE</text>

      <!-- address -->
      <path class="contact-icon" d="M40 258 L56 244 L72 258 L67 258 L67 272 L45 272 L45 258 Z"/>
      <text class="card-text contact-line" x="90" y="252">204-517 Ashgrove Ave E,</text>
      <text class="card-text contact-line" x="90" y="290">Oshawa ON L1H 4T6</text>

      <!-- phones -->
      <path class="contact-icon" d="M46 348 q-6 12 6 24 q12 12 24 6 l-4 -8 q-6 4 -14 -4 q-8 -8 -4 -14 Z"/>
      <text class="card-text contact-line" x="90" y="348">Cell :905-631-4872</text>
      <text class="card-text contact-line" x="90" y="386">Office:905-418-2096</text>

      <!-- web -->
      <g class="contact-icon">
        <circle cx="56" cy="434" r="14" fill="none" stroke="var(--ink)" stroke-width="4"/>
        <ellipse cx="56" cy="434" rx="6" ry="14" fill="none" stroke="var(--ink)" stroke-width="3"/>
        <line x1="42" y1="434" x2="70" y2="434" stroke="var(--ink)" stroke-width="3"/>
      </g>
      <text class="card-text contact-line" x="90" y="445">www.danawelloby.example</text>

      <!-- email -->
      <g class="contact-icon">
        <rect x="40" y="484" width="32" height="22"/>
        <polyline points="40,484 56,497 72,484" fill="none" stroke="var(--card-white)" stroke-width="3"/>
      </g>
      <text class="card-text contact-line" x="90" y="505">dana@homesbydana.example</text>
    </svg>
  </div>
</div>
</body>
</html>
```